Australian Legal Practice would like a Web Design

I need a web design for a newly established law practice operating as Corvin Legal.

I would like the business to have an internet presence (via a website) essentially for the purpose of marketing and advertising. As the business grows (hopefully) I may be interested in providing general legal information as a means of establishing goodwill in the community and a easy and user friends contact method through the website.

The essence of the business is personal legal service based on local knowledge and therefore i want the website to present a picture of friendly professionalism, but mostly i want people who to be able to find the contact details of the business

I would like to have a map of the office location, and photos of the front of the office, the staff (me at the moment) and picture of law themed items and featuring the Corvin Legal logo.

The areas of law which Corvin Legal practises in are as follows:

commercial law
business sale and purchases
leases
conveyancing and property law
wills and estates
powers of attorney
general legal advice
succession planning

Reason: I have not had the opportunity to properly assess the designs and provide constructive feedback. I apologise for the inconvenience caused by my delay in providing feedback. Rob K.

Target Market(s)

Potential and existing clients of the firm
Other law firms
Associated stakeholders, i.e. Banks and real estate agents

Industry/Entity Type

Law Firm

Coding

Coded - Design and coding required

Number of Pages Required

2 page

Font styles to use
Sans Serif

Colors
85acd3
33a6d7
0456a4

Requirements
Must have
• Corvin Legal logo
• Map of the office location
• Picture of Rob Corvin (principal solicitor)
• Picture of the office
• Areas of Practice
• Address of office
• email address: rob.corvin@corvinlegal-example.com.au
• Physical address: 17 Ferncliff Road, Hamilton VIC 3300
• Phone number: (03) 5683 4917
• Facsimile number: (03) 5683 4038
• Space for a brief description of the firm and its competitive advantage
• Bar Guild Logo
• Links to the Bar Guild of Victoria
• Link to the practice standards Council
Nice to have
• coded to wordpress format

```html
<!DOCTYPE html>
<html lang="en">
<head>
<meta charset="utf-8">
<title>Corvin Legal</title>
<link rel="stylesheet" href="https://fonts.googleapis.com/css2?family=Open+Sans:wght@400;600;700;800&display=swap">
<style>
:root{
  --navy:#12237c;
  --navy-dark:#0a1656;
  --navy-deep:#081244;
  --blue:#0456a4;
  --sky:#33a6d7;
  --pale:#85acd3;
  --paper:#ffffff;
  --mist:#eef0f5;
  --line:#d6dae4;
  --ink:#222a3a;
  --muted:#6b7284;
  --accent:#c9302c;
}
*{box-sizing:border-box;margin:0;padding:0}
html,body{width:1200px;height:2520px;overflow:hidden}
body{font-family:"Open Sans",Arial,sans-serif;color:var(--ink);background:var(--paper);position:relative;font-size:14px}
.wrap{position:absolute;left:88px;width:1024px}
svg{display:block}

/* top bar */
.topbar{position:absolute;top:0;left:0;width:1200px;height:40px;background:var(--navy-deep);color:#fff;font-size:13px}
.topbar .social{position:absolute;left:88px;top:10px;display:flex;gap:8px}
.dot{width:20px;height:20px;border-radius:50%;background:#fff;opacity:.9}
.topbar .contact{position:absolute;right:88px;top:10px;display:flex;gap:28px;align-items:center}
.topbar .contact span{display:flex;align-items:center;gap:6px}

/* header */
.header{position:absolute;top:40px;left:0;width:1200px;height:80px;background:var(--paper);border-bottom:1px solid var(--line)}
.nav{position:absolute;top:30px;display:flex;gap:0;font-size:13px;font-weight:600;color:var(--navy)}
.nav a{color:inherit;text-decoration:none;padding:0 12px;border-right:1px solid var(--line)}
.nav a:last-child{border-right:none}
.nav.left{left:76px}
.nav.right{right:76px}
.brand{position:absolute;left:480px;top:0;width:240px;height:110px;background:var(--paper);border:1px solid var(--line);border-top:none;display:flex;align-items:center;justify-content:center;z-index:3;box-shadow:0 4px 10px rgba(0,0,0,.08)}
.brand span{font-size:30px;font-weight:700;color:var(--navy);letter-spacing:.5px}

/* hero */
.hero{position:absolute;top:120px;left:0;width:1200px;height:500px;background:linear-gradient(120deg,#2a3352 0%,#5d6a86 40%,#c5ccd8 70%,#7f8aa2 100%)}

/* features */
.feature-band{position:absolute;top:620px;left:0;width:1200px;height:320px;background:var(--mist)}
.features{top:560px;display:grid;grid-template-columns:repeat(4,232px);gap:32px}
.feature .label{position:relative;height:100px;background:var(--navy);color:#fff;text-align:center;padding-top:46px;font-weight:700;font-size:15px;line-height:1.25}
.feature .icon{position:absolute;left:88px;top:-28px;width:56px;height:56px;border-radius:50%;background:var(--paper);border:3px solid var(--navy);display:flex;align-items:center;justify-content:center}
.feature .photo{height:200px;background:linear-gradient(160deg,#d9dde6,#8a93a8 60%,#3b4660)}

/* practice & about */
h2{font-size:18px;font-weight:700;color:var(--blue)}
.practice{top:1000px;width:472px;left:88px}
.practice p{margin-top:14px;color:var(--muted);font-size:13px;line-height:1.6}
.areas{margin-top:20px;height:290px;border:1px solid var(--line);border-left:5px solid var(--navy);padding:26px 30px;list-style:none}
.areas li{font-size:14px;line-height:2.05;color:var(--ink);display:flex;align-items:center;gap:10px}
.areas li::before{content:"";width:7px;height:7px;background:var(--accent);border-radius:50%}
.practice .photo{margin-top:30px;height:200px;background:linear-gradient(130deg,#6d768c,#c9ced9 55%,#48536b)}

.about{top:1000px;left:584px;width:528px}
.about-grid{margin-top:18px;display:grid;grid-template-columns:264px 264px;grid-template-rows:290px 280px;gap:20px 0}
.about-grid .photo-a{background:linear-gradient(150deg,#3c3530,#8b7a6a 50%,#c7b9a8)}
.about-grid .photo-b{background:linear-gradient(150deg,#e6e8ee,#9aa3b5 60%,#56607a)}
.text-box{padding:26px 24px;font-size:12.5px;line-height:1.65;color:#fff}
.text-box.blue{background:var(--navy)}
.text-box.dark{background:#1c1f26}
.text-box .more{display:block;margin-top:16px;font-weight:700}

/* cta */
.cta{top:1700px;height:120px;display:flex;background:var(--mist);border:1px solid var(--line)}
.cta .lead{width:300px;background:var(--navy-dark);color:#fff;font-size:21px;font-weight:800;line-height:1.25;padding:30px 28px;clip-path:polygon(0 0,100% 0,88% 100%,0 100%)}
.cta .call{flex:1;display:flex;align-items:center;gap:18px;padding-left:40px}
.cta .call .ring{width:58px;height:58px;border-radius:50%;border:3px solid var(--navy);display:flex;align-items:center;justify-content:center}
.cta .call small{display:block;font-size:12px;font-weight:700;color:var(--navy)}
.cta .call strong{display:block;font-size:30px;font-weight:800;color:var(--navy);line-height:1.15}
.cta .call em{display:block;font-style:normal;font-size:11px;color:var(--muted)}
.cta .chat{width:320px;background:var(--navy-dark);color:#fff;text-align:center;padding-top:26px;clip-path:polygon(10% 0,100% 0,100% 100%,0 100%)}
.cta .chat h3{font-size:18px;font-weight:800}
.cta .chat .btn{display:inline-block;margin-top:14px;background:#fff;color:var(--navy);font-weight:700;font-size:13px;padding:8px 26px;border-radius:16px}

/* results */
.results{top:1870px}
.results-grid{margin-top:22px;display:grid;grid-template-columns:repeat(4,232px);gap:32px}
.result{height:210px;border:1px solid var(--line);text-align:center;padding-top:30px;box-shadow:0 2px 6px rgba(0,0,0,.05)}
.result svg{margin:0 auto}
.result strong{display:block;margin-top:18px;font-size:32px;font-weight:700;color:var(--ink)}
.result span{display:block;margin-top:6px;font-size:12px;color:var(--muted)}

/* footer */
.footer{position:absolute;top:2200px;left:0;width:1200px;height:320px;background:var(--navy);color:#fff}
.card{position:absolute;left:88px;top:0;width:300px;height:280px;background:var(--paper);color:var(--ink);padding:22px 26px;clip-path:polygon(0 0,100% 0,100% 100%,50% 92%,0 100%)}
.card h4{font-size:14px;font-weight:800;color:var(--navy);border-bottom:2px solid var(--navy);padding-bottom:8px}
.card .firm{margin-top:16px;display:flex;align-items:center;gap:8px;font-weight:700;color:var(--navy);font-size:14px}
.card .firm i{width:12px;height:12px;background:var(--navy)}
.card p{font-size:12px;line-height:1.7;margin-top:8px}
.card .phones{color:var(--blue);font-weight:700}
.location{position:absolute;left:440px;top:28px;width:380px}
.location h4,.follow h4{font-size:13px;font-weight:800;letter-spacing:.5px}
.map{margin-top:12px;height:200px;background:linear-gradient(135deg,#e9e6dc,#cfd8c9 50%,#dfe4ea)}
.location .dir{margin-top:10px;font-size:12px}
.follow{position:absolute;left:880px;top:28px;width:232px}
.follow .social{margin-top:14px;display:flex;gap:8px}
.follow .social .dot{width:30px;height:30px}
.follow .copy{margin-top:26px;font-size:12px;opacity:.85}
</style>
</head>
<body>

<div class="topbar">
  <div class="social"><span class="dot"></span><span class="dot"></span><span class="dot"></span><span class="dot"></span></div>
  <div class="contact">
    <span><svg width="14" height="14" viewBox="0 0 24 24"><path fill="#fff" d="M6.6 10.8a15 15 0 0 0 6.6 6.6l2.2-2.2c.3-.3.7-.4 1-.2 1.1.4 2.3.6 3.6.6.6 0 1 .4 1 1V20c0 .6-.4 1-1 1A17 17 0 0 1 3 4c0-.6.4-1 1-1h3.5c.6 0 1 .4 1 1 0 1.3.2 2.5.6 3.6.1.3 0 .7-.2 1z"/></svg>(03) 5683 4917</span>
    <span><svg width="14" height="14" viewBox="0 0 24 24"><path fill="#fff" d="M2 5h20v14H2zm2 2v.5l8 5 8-5V7l-8 5z"/></svg>rob.corvin@corvinlegal-example.com.au</span>
  </div>
</div>

<header class="header">
  <nav class="nav left"><a>Home</a><a>About Us</a><a>Websites</a><a>Services</a></nav>
  <div class="brand"><span>Corvin Legal</span></div>
  <nav class="nav right"><a>Practice Areas</a><a>Case Results</a><a>Contact Us</a></nav>
</header>

<div class="hero" role="img" aria-label="Business lawyers shaking hands in a bright office"></div>

<div class="feature-band"></div>
<section class="wrap features">
  <div class="feature">
    <div class="label"><span class="icon"><svg width="30" height="30" viewBox="0 0 24 24" fill="none" stroke="#12237c" stroke-width="1.8"><path d="M12 3v18M6 21h12M4 7h16M6 7l-3 7h6zM18 7l-3 7h6z"/></svg></span>Why we are<br>different</div>
    <div class="photo" role="img" aria-label="Solicitor seated at a desk"></div>
  </div>
  <div class="feature">
    <div class="label"><span class="icon"><svg width="30" height="30" viewBox="0 0 24 24" fill="none" stroke="#12237c" stroke-width="1.8"><path d="M3 9l9-5 9 5H3zM5 9v9M9.5 9v9M14.5 9v9M19 9v9M3 20h18"/></svg></span>Personal<br>Injury</div>
    <div class="photo" role="img" aria-label="Client meeting with a lawyer"></div>
  </div>
  <div class="feature">
    <div class="label"><span class="icon"><svg width="30" height="30" viewBox="0 0 24 24" fill="none" stroke="#12237c" stroke-width="1.8"><rect x="3" y="7" width="18" height="13" rx="1"/><path d="M9 7V4h6v3M3 12h18"/></svg></span>Business<br>Disputes</div>
    <div class="photo" role="img" aria-label="Business colleagues discussing a contract"></div>
  </div>
  <div class="feature">
    <div class="label"><span class="icon"><svg width="30" height="30" viewBox="0 0 24 24" fill="none" stroke="#12237c" stroke-width="1.8"><path d="M4 20h16M6 20v-6M11 20V9M16 20V5"/></svg></span>Our<br>Results</div>
    <div class="photo" role="img" aria-label="Lawyers reviewing documents together"></div>
  </div>
</section>

<section class="wrap practice">
  <h2>Practice Areas</h2>
  <p>If you need sound, local advice, our team is ready to help. We take time to understand your matter and explain every option in plain language before you decide.</p>
  <ul class="areas">
    <li>Commercial law</li>
    <li>Business sale and purchases</li>
    <li>Leases</li>
    <li>Conveyancing and property law</li>
    <li>Wills and estates</li>
    <li>Powers of attorney</li>
    <li>General legal advice</li>
    <li>Succession planning</li>
  </ul>
  <div class="photo" role="img" aria-label="Legal team meeting around a table"></div>
</section>

<section class="wrap about">
  <h2>About Us</h2>
  <div class="about-grid">
    <div class="photo-a" role="img" aria-label="Lawyers consulting in a library"></div>
    <div class="text-box blue">Corvin Legal is a new local practice built on personal service. We know the region, its people and its businesses, and we give clear advice you can act on with confidence.<span class="more">Read More</span></div>
    <div class="text-box dark">Our principal works with clients directly from the first call to the final result. You deal with one lawyer who knows your file, returns calls promptly and keeps fees transparent.<span class="more">Read More</span></div>
    <div class="photo-b" role="img" aria-label="Portrait of the principal solicitor"></div>
  </div>
</section>

<section class="wrap cta">
  <div class="lead">GET FREE LEGAL<br>CONSULTATION:</div>
  <div class="call">
    <span class="ring"><svg width="28" height="28" viewBox="0 0 24 24"><path fill="#12237c" d="M6.6 10.8a15 15 0 0 0 6.6 6.6l2.2-2.2c.3-.3.7-.4 1-.2 1.1.4 2.3.6 3.6.6.6 0 1 .4 1 1V20c0 .6-.4 1-1 1A17 17 0 0 1 3 4c0-.6.4-1 1-1h3.5c.6 0 1 .4 1 1 0 1.3.2 2.5.6 3.6.1.3 0 .7-.2 1z"/></svg></span>
    <div><small>CALL US TOLL FREE:</small><strong>(03) 5683 4917</strong><em>Mon to Fri, 9:00 am to 5:00 pm, no charge</em></div>
  </div>
  <div class="chat"><h3>ONLINE SUPPORT CHAT</h3><span class="btn">Register Now!</span></div>
</section>

<section class="wrap results">
  <h2>Case Results</h2>
  <div class="results-grid">
    <div class="result"><svg width="44" height="44" viewBox="0 0 24 24" fill="none" stroke="#222a3a" stroke-width="1.8"><path d="M12 3l10 18H2z"/><path d="M12 10v5M12 17.5v.5"/></svg><strong>$3,750,000</strong><span>Slip and Fall Incident</span></div>
    <div class="result"><svg width="44" height="44" viewBox="0 0 24 24" fill="none" stroke="#222a3a" stroke-width="1.8"><path d="M14 6a4 4 0 0 1 5-3l-3 3 2 2 3-3a4 4 0 0 1-5 5L7 19a2 2 0 0 1-3-3z"/></svg><strong>$1,500,000</strong><span>Construction Accident</span></div>
    <div class="result"><svg width="44" height="44" viewBox="0 0 24 24" fill="none" stroke="#222a3a" stroke-width="1.8"><path d="M3 7l9-4 9 4v10l-9 4-9-4zM3 7l9 4 9-4M12 11v10"/></svg><strong>$700,000</strong><span>Falling Box Incident</span></div>
    <div class="result"><svg width="44" height="44" viewBox="0 0 24 24" fill="none" stroke="#222a3a" stroke-width="1.8"><path d="M3 16v-4l2-5h14l2 5v4zM3 12h18"/><circle cx="7" cy="17" r="2"/><circle cx="17" cy="17" r="2"/></svg><strong>$625,000</strong><span>Motor Vehicle Accident</span></div>
  </div>
</section>

<footer class="footer">
  <div class="card">
    <h4>CONTACT INFORMATIONS</h4>
    <div class="firm"><i></i>CORVIN LEGAL</div>
    <p>17 Ferncliff Road, Hamilton VIC 3300<br>Australia</p>
    <p class="phones">(03) 5683 4917<br>(03) 5683 4038</p>
    <p>Email: rob.corvin@corvinlegal-example.com.au</p>
  </div>
  <div class="location">
    <h4>LOCATION</h4>
    <div class="map" role="img" aria-label="Street map showing the office location in Hamilton"></div>
    <p class="dir">Click Here For Directions</p>
  </div>
  <div class="follow">
    <h4>FOLLOW US</h4>
    <div class="social"><span class="dot"></span><span class="dot"></span><span class="dot"></span><span class="dot"></span></div>
    <p class="copy">© Corvin Legal 2014 | Site Map</p>
  </div>
</footer>

</body>
</html>
```